Wine Label for White and Red Wine from California

We need a wine label for 2 whites and 2 red wines. (Merlot, Cabernet Sauvignon, Chardonnay, Pinot Grigio) Can be the same label or can have something to differentiate among them such as a color change. This is a label for an already existing wine on the US market but needs to be completely re-done. We want something way sharper, eye catching. Don't use the original label please as your starting point-- I don't think we want to see it anymore. But the structure of it is ok and the fonts are ok. (The tree is what is so awful about)

Target Market(s)

US market, always good to think of millennials, but still appeal to all ages. Men and women.

Colors

Designer to choose colors to be used in the design.

Requirements
Must have
• Should be eye catching, grabs attention, looks expensive, sells for a value price. Should feature the brand name and varietal and vintage:
• Dorvane Vineyards / Cabernet Sauvignon / 2014
• Bottle type is the 'Bordeaux Style' bottle. The white wine is a green bottle, the red wine uses a dark brown bottle. Be sure the labels look good on these bottles.
• What this bottle looks like is shown below.
• The label we are replacing is shown in the briefs.
Nice to have
• We feel successful labels have a lot of white background, stay away from dark labels-- they scratch too much when handled.
• Attached is a label we like, please look at the Cadenza label image below. But at the same time, we are flexible to your creativity. But nothing too crazy please.
Should not have
• Should not have a dark background.
• We are not big fans of grapes on the label unless extremely stylised. Nor do we like wine glasses, wine bottles.

```html
<!DOCTYPE html>
<html lang="en">
<head>
<meta charset="utf-8">
<title>Dorvane Vineyards – Pinot Grigio Label</title>
<link rel="stylesheet" href="https://fonts.googleapis.com/css2?family=Cinzel:wght@400;600;700&family=Cormorant+Garamond:ital,wght@1,500&family=Pinyon+Script&display=swap">
<style>
  :root {
    --backdrop: #ffffff;
    --paper: #eeeeea;
    --paper-edge: #e2e2dc;
    --ink: #1c1c1c;
    --gold: #b8923a;
    --gold-light: #e0c27a;
    --gold-deep: #8a6a22;
  }
  * { margin: 0; padding: 0; box-sizing: border-box; }
  html, body {
    width: 1200px;
    height: 1200px;
    overflow: hidden;
    background: var(--backdrop);
  }
  .canvas {
    width: 1200px;
    height: 1200px;
    display: flex;
    align-items: center;
    justify-content: center;
  }
  .wine-label {
    width: 840px;
    height: 950px;
    background: var(--paper);
    box-shadow: inset 0 0 0 1px var(--paper-edge);
    display: flex;
    flex-direction: column;
    align-items: center;
    padding-top: 82px;
  }
  .ornament {
    background: linear-gradient(90deg, transparent 0%, var(--gold-deep) 15%, var(--gold-light) 50%, var(--gold-deep) 85%, transparent 100%);
    opacity: 0.55;
  }
  .ornament-top {
    width: 560px;
    height: 150px;
    border-radius: 50% 50% 10% 10% / 60% 60% 20% 20%;
    opacity: 0.35;
  }
  .brand-name {
    margin-top: 30px;
    font-family: "Cinzel", serif;
    font-weight: 400;
    font-size: 96px;
    line-height: 1.12;
    letter-spacing: 2px;
    color: var(--ink);
    text-align: center;
  }
  .brand-name span { display: block; }
  .varietal {
    margin-top: 26px;
    font-family: "Cinzel", serif;
    font-weight: 700;
    font-size: 28px;
    letter-spacing: 2px;
    color: var(--ink);
  }
  .appellation {
    margin-top: 4px;
    font-family: "Pinyon Script", cursive;
    font-size: 62px;
    line-height: 1;
    color: var(--gold);
  }
  .vintage {
    margin-top: 2px;
    font-family: "Cormorant Garamond", serif;
    font-style: italic;
    font-weight: 500;
    font-size: 34px;
    letter-spacing: 3px;
    color: var(--ink);
  }
  .ornament-bottom {
    margin-top: 22px;
    width: 420px;
    height: 70px;
    border-radius: 10% 10% 50% 50% / 20% 20% 60% 60%;
    opacity: 0.35;
  }
</style>
</head>
<body>
  <main class="canvas">
    <section class="wine-label">
      <div class="ornament ornament-top" role="img" aria-label="Gold calligraphic flourish crowning the brand name"></div>
      <h1 class="brand-name"><span>Dorvane</span><span>Vineyards</span></h1>
      <p class="varietal">PINOT GRIGIO</p>
      <p class="appellation">Napa Valley</p>
      <p class="vintage">2010</p>
      <div class="ornament ornament-bottom" role="img" aria-label="Gold calligraphic flourish beneath the vintage"></div>
    </section>
  </main>
</body>
</html>
```